FINANCIAL MANAGEMENT COMPANY LOGO

LOGO, BUSINESS CARD & STATIONERY

NEW FINANCIAL MANAGEMENT COMPANY

name: BRAMBLE Financial Management Pty Ltd
abn xx xxx xxx xxx
address: (not yet available)
Telephone: (not yet available)

Strategic Financial Planning and Management Company

- Superannuation
- SMSF (Own Fund)
- Retail/Industry Funds (fund controlled)

- Personal Wealth
- Planning
- Forcasting
- Portfolio Management

- Future Generations
- Strategy
- Structural Implimenation and Management

- Risk Insurance
- Analysis
- Implimentation
- Review

NOTES:
I would like to project professionalism, security and personal care.
Comforting, warm colours

Name on Business card:

Marion Tate
FPRB Authorised Financial Strategist

THANK YOU FOR THE SUBMISSIONS .......
I WOULD LIKE TO SEE EARTHY AND  RELAXED TONES WITH AN UNDERSTANDING OF AN 'ALL INCLUSIVE  & CARING' FEEL.
REALLY APPRECIATE ALL THE  IDEAS SO FAR....

Target Market(s)

Middle aged, reasonably wealthy, successful,

Industry/Entity Type

Security

Logo Text

BRAMBLE Financial Management Pty Ltd

Logo styles of interest
Abstract Logo
Requirements
Must have
• business card to carry full deatils of company and it's services (as previously described in this brief)
Nice to have
• Logo to be easily recognised on all stationey and advertising boards

```html
<!DOCTYPE html>
<html lang="en">
<head>
<meta charset="utf-8">
<title>Bramble Financial Management – Letterhead</title>
<link rel="stylesheet" href="https://fonts.googleapis.com/css2?family=Marcellus&family=Oswald:wght@400;500&display=swap">
<style>
  :root {
    --bark: #43230f;
    --cream: #f1e7cc;
    --leaf: #7d9a2e;
    --olive: #8c7f58;
    --sand: #a89e7c;
    --frame: #222;
    --paper: #fff;
  }
  html, body { margin: 0; padding: 0; overflow: hidden; }
  body { width: 932px; height: 1200px; background: var(--paper); }
  .letterhead { position: relative; width: 932px; height: 1200px; }
  .page-frame {
    position: absolute; left: 9px; top: 9px; width: 912px; height: 1181px;
    border: 1px solid var(--frame); box-sizing: border-box;
  }
  .header-shape { position: absolute; left: 0; top: 0; }
  .brand {
    position: absolute; left: 87px; width: 275px; top: 104px;
    text-align: center; font-family: "Marcellus", serif; color: var(--cream);
  }
  .brand-name { margin: 0; font-weight: 400; line-height: 1; }
  .brand-main { display: block; font-size: 40px; letter-spacing: 1px; }
  .brand-sub { display: block; font-size: 10.5px; letter-spacing: 0.3px; margin-top: 4px; }
  .brand-rule { width: 130px; height: 1px; background: var(--leaf); margin: 3px auto 3px; }
  .brand-abn { font-size: 9px; color: var(--olive); letter-spacing: 0.5px; }
  .services {
    position: absolute; left: 381px; top: 170px; margin: 0; padding: 0;
    list-style: none; display: flex; gap: 16px;
    font-family: "Oswald", sans-serif; font-size: 14px; color: var(--cream);
  }
  .services li { display: flex; align-items: center; gap: 3px; }
  .services .bullet {
    width: 11px; height: 4px; border-radius: 50%; background: var(--leaf);
    transform: rotate(-12deg);
  }
  .disclaimer {
    position: absolute; left: 142px; top: 1115px; width: 646px; height: 44px;
    background: var(--sand); color: var(--bark); text-align: center;
    font-family: "Oswald", sans-serif; font-weight: 500; font-size: 12px; line-height: 16px;
    display: flex; flex-direction: column; justify-content: center;
  }
  .disclaimer p { margin: 0; }
</style>
</head>
<body>
<div class="letterhead">
  <div class="page-frame"></div>

  <svg class="header-shape" width="932" height="200" viewBox="0 0 932 200" aria-hidden="true">
    <path d="M87 197 A145 125 0 0 1 358 161 L845 161 L845 197 Z" fill="var(--bark)"/>
  </svg>

  <div class="brand">
    <h1 class="brand-name">
      <span class="brand-main">BRAMBLE</span>
      <span class="brand-sub">FINANCIAL MANAGEMENT PTY LTD</span>
    </h1>
    <div class="brand-rule"></div>
    <div class="brand-abn">ABN xx xxx xxx xxx</div>
  </div>

  <ul class="services">
    <li><span class="bullet"></span>Superannuation</li>
    <li><span class="bullet"></span>Investment</li>
    <li><span class="bullet"></span>Wealth Creation</li>
    <li><span class="bullet"></span>Risk</li>
    <li><span class="bullet"></span>Estate Planning</li>
  </ul>

  <footer class="disclaimer">
    <p>Bramble Financial Management Pty Ltd is a Corporate Authorised Representative of Meridian7 Financial Services Pty Ltd Abn 47 318 602 115</p>
    <p>Australian Financial Services Licensee - Licence Number 318864 4/22 Kestrel Street, QLD 4109</p>
  </footer>
</div>
</body>
</html>
```